Stellenanzeigen zur Mitarbeitergewinnung über soziale Medien & Google / YouTube
Zielgruppe
Wir sind zwei Brüder und Inhaber der Zahnarztpraxis „ Zahnmedizin am Lindenhof“ in Bochum.
Wir benötigen zur Mitarbeitergewinnung ein neues, modernes Konzept. Insbesondere stehen Stellenanzeigen im Vordergrund, die in sozialen Medien, wie Instagram, aber auch über Google und YouTube angezeigt werden sollen und potentielle Mitarbeiter auf unsere eigene Landingpage zur Mitarbeitergewinnung führen
Es geht nicht darum, Patienten anzusprechen, sondern ausschließlich um Mitarbeitergewinnung.
Aufgabenstellung
Wir haben Interesse an einem Gesamtkonzept, eine Serie von Anzeigen, die unsere Praxis widerspiegeln, uns als Inhaber zeigen, sowie unsere vorhandenen Mitarbeiterinnen einbinden.
Aufgrund der Vielzahl von Stellenanzeigen im medizinischen Bereich, braucht es neue Ideen. Wir möchten uns deutlich von den vorhandenen, unzähligen Anzeigen bei Instagram abheben. Hier sind kreative Ideen erwünscht.
Wir haben eine zur Mitarbeitergewinnung vorhandene Homepage, die Videos und Aussagekräftige Fotos und Texte beinhaltet. Dort gibt es die Möglichkeit, sich direkt auf eine freie Stelle unkompliziert zu bewerben.
Wir möchten über die neuen Anzeigen potentielle Mitarbeiter dazu bewegen, sich diese Homepage anzusehen und sich gegebenfalls direkt zu bewerben.
Wir freuen uns über ein Gesamtkonzept, gerne verschiedene Stellenanzeigen, die aber ineinander schlüssig sind. Beispielsweise mit anderen Überschriften oder mit verschiedenen Fotos, die wir bereitstellen. Die vorgeschlagenen Fotos können gerne benutzt werden, alternativ sind wir im Hinblick auf das Gesamtkonzept auch offen für andere Ideen und Fotos. Da die Mitbewerbersituation extrem hoch ist, macht es Sinn, sich vorhandene Stellenanzeigen anzusehen, damit wir deutlich die Vorteile unserer Praxis transportieren und uns klar positionieren.
Wir Inhaber, Brüder, Dr. Tobias und Lars Wendrich, sind Ende 30, Ruhrpottkinder, haben eine moderne Praxis zentral in Bochum am Eichgarten.
Unsere Praxis ist im modernen und ansprechenden Lindenhof. Wir haben bereits ein großes Team und zwei weitere angestellte Zahnärztinnen. Bei uns gibt es eine faire Bezahlung, Zusatzleistungen, die eine Gutscheinkarte oder die Möglichkeit eines Stellplatzes oder ÖPNV Ticket. Wir machen keine Überstunden, sind freundliche und entspannte Chefs. Wir legen Wert auf Qualität und nehmen uns für uns Zeit für Patienten und Mitarbeiter.
Ziel sollte es sein, motivierte und leistungsstarke Mita..

```html
<!DOCTYPE html>
<html lang="de">
<head>
<meta charset="utf-8">
<title>Stellenanzeige – Zahnmedizin am Lindenhof</title>
<link href="https://fonts.googleapis.com/css2?family=Jost:wght@400;500;600;700&display=swap" rel="stylesheet">
<style>
  :root {
    --orange-light: #f6b500;
    --orange-deep: #f29400;
    --ghost: rgba(255, 214, 80, 0.28);
    --white: #ffffff;
    --teal: #17b8a7;
    --brand-ink: #2b2b2b;
    --brand-square: #b9ad93;
  }
  * { box-sizing: border-box; margin: 0; padding: 0; }
  html, body { width: 1200px; height: 1200px; overflow: hidden; }
  body { font-family: "Jost", sans-serif; }

  .ad {
    position: relative;
    width: 1200px;
    height: 1200px;
    overflow: hidden;
    background: linear-gradient(160deg, var(--orange-light) 0%, var(--orange-deep) 100%);
    color: var(--white);
  }

  .ghost-words {
    position: absolute;
    left: 20px;
    top: 30px;
    font-weight: 700;
    font-size: 215px;
    line-height: 0.93;
    letter-spacing: 4px;
    color: var(--ghost);
    white-space: nowrap;
    text-transform: uppercase;
  }

  .headline {
    position: absolute;
    left: 112px;
    top: 106px;
    text-transform: uppercase;
    line-height: 1;
  }
  .headline .lead { display: block; font-weight: 400; font-size: 127px; letter-spacing: 1px; }
  .headline .strong { display: block; font-weight: 700; font-size: 133px; margin-top: 16px; letter-spacing: 1px; }

  .subline {
    position: absolute;
    left: 114px;
    top: 452px;
    font-weight: 500;
    font-size: 88px;
    line-height: 86px;
  }

  .brand {
    position: absolute;
    left: 888px;
    top: -20px;
    width: 266px;
    height: 258px;
    background: var(--white);
    border-radius: 20px;
    color: var(--brand-ink);
    display: flex;
    flex-direction: column;
    align-items: center;
    justify-content: center;
    padding-top: 20px;
    gap: 16px;
  }
  .brand .mark {
    width: 34px;
    height: 34px;
    background: var(--brand-square);
  }
  .brand .name {
    font-weight: 500;
    font-size: 30px;
    line-height: 34px;
    text-align: center;
  }

  .portrait { position: absolute; left: 472px; top: 244px; }

  .cta-arrow { position: absolute; left: 168px; top: 948px; }

  .cta-band {
    position: absolute;
    left: 0;
    bottom: 0;
    width: 1200px;
    height: 190px;
    background: var(--teal);
    clip-path: inset(0 0 0 300px round 60px 0 0 0);
  }
  .cta-text {
    position: absolute;
    right: 102px;
    bottom: 30px;
    font-weight: 500;
    font-size: 59px;
    color: var(--white);
    white-space: nowrap;
  }
</style>
</head>
<body>
  <main class="ad">
    <div class="ghost-words" aria-hidden="true">Du hast<br>etwas<br>Besseres<br>verdient</div>

    <h1 class="headline">
      <span class="lead">Bist du die</span>
      <span class="strong">Beste?</span>
    </h1>

    <p class="subline">Beweise es<br>in unserem<br>leistungs-<br>starken<br>Team</p>

    <svg class="portrait" width="680" height="780" viewBox="0 0 680 780" role="img" aria-label="Foto eines Praxisinhabers im hellblauen Poloshirt mit Lupenbrille, Arme verschränkt">
      <defs>
        <linearGradient id="portraitFill" x1="0" y1="0" x2="0" y2="1">
          <stop offset="0" stop-color="#d9a98a"/>
          <stop offset="0.4" stop-color="#e6ecf3"/>
          <stop offset="1" stop-color="#c9d3de"/>
        </linearGradient>
      </defs>
      <path d="M215 150 C215 40 345 -5 425 30 C500 60 520 140 505 230 C495 290 480 330 470 350 C540 370 610 420 630 480 C660 580 670 680 675 780 L15 780 C20 680 25 580 45 500 C60 430 140 380 230 350 C220 300 215 230 215 150 Z"
            fill="url(#portraitFill)" stroke="#ffffff" stroke-width="10" stroke-linejoin="round"/>
    </svg>

    <div class="brand">
      <span class="mark" aria-hidden="true"></span>
      <p class="name">Zahnmedizin<br>am Lindenhof</p>
    </div>

    <div class="cta-band"></div>

    <svg class="cta-arrow" width="150" height="170" viewBox="0 0 150 170" aria-hidden="true">
      <path d="M10 10 C40 50 70 80 95 105 L80 118 L138 150 L120 88 L108 100 C85 72 60 40 36 0 Z"
            fill="none" stroke="#ffffff" stroke-width="5" stroke-linejoin="round"/>
    </svg>

    <p class="cta-text">Klick für exklusive Einblicke!</p>
  </main>
</body>
</html>
```